Vantel Solutions Website Design

We are a B2B startup offering a free virtual data room and deal management platform for small businesses. We need a 10-page website geared towards business executives and entrepreneurs that is simple, uploads quickly and provides a good introduction to our product. We've attached a document setting forth the text of 8 of the 10 pages (the other two - Resources and Blog - need to be designed to allow the future posting of white papers and blog entries) and links to the screenshots and GIFs, all of which are in a folder on filewell. We've also attached a zip file with our logo and a pdf file with our font and colors. Examples of websites we like include www.marbletoft.example, www.usepivra.example and https://kelmo.example.

Target Market(s)

Small business owners, business executives and entrepreneurs

Industry/Entity Type

Finance

Coding

Number of Pages Required

5+ page

Font styles to use
Sans Serif

Colors
85abd2
f9ba93

Requirements
Must have
• Please use the Wordpress harbor theme I uploaded to code the site.
Nice to have
• Clean, uncluttered design. White background. Screenshots and gifs should be shown on monitors (desktop, laptop and iPad only). Blue and orange are our corporate colors, but you’re not limited to those two colors. See uploaded logo guide for complementary colors or use your own judgment.

```html
<!DOCTYPE html>
<html lang="en">
<head>
<meta charset="utf-8">
<title>Vantel – Workflow Management</title>
<link href="https://fonts.googleapis.com/css2?family=Montserrat:wght@400;500;600;700&display=swap" rel="stylesheet">
<style>
  :root{
    --blue:#85abd2;
    --blue-deep:#4f7fae;
    --logo-blue:#3f6f9f;
    --orange:#f9ba93;
    --ink:#1f2630;
    --muted:#3b4450;
    --grey-band:#ececec;
    --white:#ffffff;
    --hero-a:#2b3138;
    --hero-b:#4c5560;
  }
  *{box-sizing:border-box;margin:0;padding:0}
  html,body{width:1200px;height:1200px;overflow:hidden;background:var(--white)}
  body{font-family:"Montserrat",sans-serif;color:var(--ink);position:relative}
  .page{position:absolute;left:441px;top:0;width:318px;height:1200px;background:var(--white)}
  .abs{position:absolute}

  /* header */
  .brand{font-weight:600;color:var(--logo-blue);font-size:11px;letter-spacing:-.2px}
  .site-header .brand{left:35px;top:7px}
  .nav{left:118px;top:10px;font-size:4.6px;color:var(--ink)}
  .btn-outline{left:246px;top:8px;width:37px;height:11px;border:0.8px solid var(--blue);color:var(--blue);font-size:4.4px;display:flex;align-items:center;justify-content:center}

  /* hero */
  .hero{left:0;top:26px;width:318px;height:144px;background:linear-gradient(120deg,var(--hero-a),var(--hero-b) 60%,#3a4048)}
  .hero h1{left:34px;top:24px;width:150px;font-size:11.8px;line-height:14.2px;font-weight:600;color:var(--white)}
  .hero p{left:35px;top:72px;width:150px;font-size:7.4px;line-height:9.4px;color:#e6e9ee}
  .btn-orange{background:var(--orange);color:var(--ink);font-size:6.4px;display:flex;align-items:center;justify-content:center}
  .hero .btn-orange{left:35px;top:110px;width:58px;height:16px}

  /* intro */
  .device{left:29px;top:218px;width:128px;height:78px;border-radius:4px;background:linear-gradient(180deg,#3a3d42,#9da3aa)}
  .intro h2{left:182px;top:192px;width:110px;font-size:7.6px;line-height:9.4px;font-weight:600}
  .intro .lede{left:182px;top:218px;width:110px;font-size:5.4px;line-height:7.2px;color:var(--muted)}
  .intro .lede b{color:var(--ink)}
  .ticks{left:182px;top:266px;width:110px;list-style:none}
  .ticks li{display:flex;gap:4px;font-size:5.1px;line-height:6.6px;color:var(--muted);margin-bottom:5.4px}
  .ticks svg{flex:none;width:7px;height:7px;margin-top:2px}

  /* band */
  .band{left:0;top:334px;width:318px;height:104px;background:linear-gradient(100deg,#93b3d6,#7fa5cc)}
  .band p{left:34px;top:35px;width:134px;font-size:6.9px;line-height:8.4px;color:var(--ink)}
  .shot{background:linear-gradient(180deg,#4f7fae 0 7%,#f4f6f9 7%);border:1px solid #dfe5ec}

  /* features */
  .features h3{left:0;top:452px;width:318px;text-align:center;font-size:7.2px;line-height:8.4px;font-weight:600}
  .features h3 span{font-weight:400;display:block;font-size:6.8px}
  .feat{width:80px;text-align:center}
  .feat svg{display:block;margin:0 auto 10px;width:16px;height:16px}
  .feat h4{font-size:5.9px;font-weight:600;margin-bottom:2px}
  .feat p{font-size:4.6px;line-height:5.9px;color:var(--muted)}

  /* quote */
  .quote{left:0;top:649px;width:318px;height:56px;background:var(--grey-band);text-align:center}
  .quote p{position:absolute;left:30px;top:14px;width:258px;font-size:7.3px;line-height:8.8px}
  .quote small{position:absolute;left:0;top:37px;width:318px;font-size:4.4px;color:var(--muted)}

  /* benefits */
  .benefits{left:0;top:705px;width:318px;height:405px;background:var(--blue)}
  .benefit{text-align:center;width:118px}
  .benefit h4{font-size:6.8px;font-weight:600;margin-bottom:4px}
  .benefit p{font-size:4.9px;line-height:6.2px;color:var(--ink)}

  /* cta */
  .cta p{left:60px;top:1123px;width:198px;text-align:center;font-size:6.9px;line-height:8.3px}
  .cta .btn-orange{left:134px;top:1147px;width:50px;height:14px;font-size:6.2px}

  /* footer */
  .site-footer{left:0;top:1173px;width:318px;height:27px;background:var(--grey-band)}
  .site-footer .brand{left:35px;top:6px}
  .site-footer small{position:absolute;left:124px;top:11px;font-size:3.8px}
  .social{left:244px;top:11px;display:flex;gap:3px}
  .social i{display:block;width:5px;height:5px;background:var(--blue)}
</style>
</head>
<body>
<main class="page">

  <header class="site-header">
    <div class="abs brand">Vantel</div>
    <nav class="abs nav">Features | Our Clients | Company | Contact Us</nav>
    <div class="abs btn-outline">Try it Now</div>
  </header>

  <section class="abs hero" role="img" aria-label="Photo of a person working at a laptop beside a coffee cup, darkened">
    <h1 class="abs">Simplify workflow management with Vantel</h1>
    <p class="abs">Free business process management software built for collaboration and easy customization</p>
    <div class="abs btn-orange">Try it today!</div>
  </section>

  <section class="intro">
    <div class="abs device" role="img" aria-label="Laptop showing the Vantel dashboard"></div>
    <h2 class="abs">Manage Your Workflow Better with Vantel</h2>
    <p class="abs lede"><b>The Vantel Assistant</b> is a secure, sharable workflow management platform designed with your needs in mind. Here are some features you'll love:</p>
    <ul class="abs ticks">
      <li><svg viewBox="0 0 10 10"><circle cx="5" cy="5" r="5" fill="#85abd2"/><path d="M2.6 5.2l1.7 1.6 3.2-3.4" stroke="#fff" stroke-width="1.2" fill="none"/></svg>Built for internal and external collaboration</li>
      <li><svg viewBox="0 0 10 10"><circle cx="5" cy="5" r="5" fill="#85abd2"/><path d="M2.6 5.2l1.7 1.6 3.2-3.4" stroke="#fff" stroke-width="1.2" fill="none"/></svg>Highly customizable and intuitive</li>
      <li><svg viewBox="0 0 10 10"><circle cx="5" cy="5" r="5" fill="#85abd2"/><path d="M2.6 5.2l1.7 1.6 3.2-3.4" stroke="#fff" stroke-width="1.2" fill="none"/></svg>Free to use – no setup or monthly fees</li>
    </ul>
  </section>

  <section class="abs band" role="img" aria-label="Soft blue-tinted office photo background">
    <p class="abs">If you want to process contracts faster while reducing costs (did we mention that it was free?), <b>Vantel</b> is the ideal solution for you.</p>
    <div class="abs shot" style="left:177px;top:24px;width:106px;height:59px" role="img" aria-label="Vantel screenshot with video play prompt"></div>
  </section>

  <section class="features">
    <h3 class="abs">Features At-a-Glance User-friendly workflow<span>Management software that saves time<br>and money</span></h3>

    <div class="abs feat" style="left:32px;top:494px">
      <svg viewBox="0 0 16 16" fill="none" stroke="#85abd2" stroke-width="1.2"><path d="M3 6h8M3 9h8M3 12h8M3 15h8"/><path d="M10 4l2-3M12 5l3-2"/></svg>
      <h4>Workflow Management</h4><p>Efficiently handle multi-party transactions with customizable, collaborative workflow software.</p>
    </div>
    <div class="abs feat" style="left:118px;top:494px">
      <svg viewBox="0 0 16 16" fill="none" stroke="#85abd2" stroke-width="1.4"><rect x="2" y="3" width="11" height="11"/><path d="M5 8l3 3 7-8"/></svg>
      <h4>Built-in Checklists</h4><p>Swap old process checklists for online checklists linked to documents housed in our secure database.</p>
    </div>
    <div class="abs feat" style="left:205px;top:494px">
      <svg viewBox="0 0 16 16" fill="#85abd2" stroke="#85abd2" stroke-width="1.2"><circle cx="12" cy="4" r="2.2"/><circle cx="4" cy="8" r="2.2"/><circle cx="12" cy="12" r="2.2"/><path d="M12 4L4 8l8 4" fill="none"/></svg>
      <h4>Real-time Sharing</h4><p>Automate new file requests and enable real-time downloads from a single self-service portal.</p>
    </div>
    <div class="abs feat" style="left:32px;top:578px">
      <svg viewBox="0 0 16 16" fill="none" stroke="#85abd2" stroke-width="1.2"><path d="M4 12l8-8M8 4h4v4M8 12H4V8"/></svg>
      <h4>Better Transparency</h4><p>Make all of your files visible to your team instantly from a secure, cloud-based sharing environment.</p>
    </div>
    <div class="abs feat" style="left:118px;top:578px">
      <svg viewBox="0 0 16 16" fill="none" stroke="#85abd2" stroke-width="1.4"><rect x="1.5" y="4" width="13" height="8"/><circle cx="8" cy="8" r="2.2"/></svg>
      <h4>Lower Costs</h4><p>Share your files from anywhere with anyone from a single, easy-to-use platform.</p>
    </div>
    <div class="abs feat" style="left:205px;top:578px">
      <svg viewBox="0 0 16 16" fill="#85abd2"><path d="M5 7V5a3 3 0 016 0v2" fill="none" stroke="#85abd2" stroke-width="1.4"/><rect x="3.5" y="7" width="9" height="8" rx="1"/></svg>
      <h4>End-to-end Security</h4><p>Host your data on encrypted Nimbara servers complete with user authentication and tracking.</p>
    </div>
  </section>

  <section class="abs quote">
    <p>“Efficient workflow management has resulted in an 85% savings in deal closings over the past six years.”</p>
    <small>- The Global Council for Contract Operations -</small>
  </section>

  <section class="abs benefits">
    <div class="abs benefit" style="left:32px;top:33px"><h4>Waste Less, Do More</h4><p>Reduce administrative costs by streamlining workflows and automating document storage and sharing from a single, cloud-based platform.</p></div>
    <div class="abs shot" style="left:177px;top:21px;width:106px;height:57px" role="img" aria-label="Vantel screenshot with video play prompt"></div>

    <div class="abs shot" style="left:34px;top:105px;width:122px;height:66px" role="img" aria-label="Vantel dashboard screenshot"></div>
    <div class="abs benefit" style="left:167px;top:115px"><h4>Simplify Your Workflow</h4><p>Manage your documents using visual cues and tools you're already familiar with - from process templates to customized checklists, reports on user activity, and more</p></div>

    <div class="abs benefit" style="left:35px;top:219px"><h4>Communicate Better</h4><p>Share unlimited stored documents with your team and those outside your organization from an online portal with user permissions you define.</p></div>
    <div class="abs shot" style="left:162px;top:203px;width:123px;height:66px" role="img" aria-label="Vantel document portal screenshot"></div>

    <div class="abs shot" style="left:34px;top:298px;width:122px;height:66px" role="img" aria-label="Vantel contract list screenshot"></div>
    <div class="abs benefit" style="left:167px;top:311px"><h4>Keep Customers Happy</h4><p>Look up contract details, locate files, and share documents with a few clicks while providing a better customer experience</p></div>
  </section>

  <section class="cta">
    <p class="abs">Manage Your Workflow with Vantel Try it today. You'll wonder how you got by without it.</p>
    <div class="abs btn-orange">Try it today</div>
  </section>

  <footer class="abs site-footer">
    <div class="abs brand">Vantel</div>
    <small>Copyright 2017. All Rights Reserved</small>
    <div class="abs social"><i></i><i></i><i></i><i></i><i></i></div>
  </footer>

</main>
</body>
</html>
```